Design for Pediatric Occupational Therapist who works with children with special needs

I need 2 x 2 sq business cards and post cards for my Pediatric Occupational Therapy business. We work with children with special needs and help them learn skills for daily living (eating, writing, dressing, etc). We're looking for a colorful design (not loud) that looks professional and helps it stand out from other cards. I want to avoid many of the standard designs that you see on Nimbo press which are used my many other Pediatric OT's. The design will be intended for business cards, post cards and hopefully can also be used on company letterhead. I'll upload a current copy of the logo we currently use on company letter head so you get an idea of the design we've been using to date. This image does not need to be used again, but serves more as a reference to the design used in the past. The winning designer will likely be hired to design a custom logo for letter head.
Updates

Project Deadline Extended Reason: I want to extend the deadline to allow for more designs and review time. Added Sunday, January 8, 2017

Target Market(s)

Families of children with special needs, pediatricians

Industry/Entity Type

Business

Contact Information for Business Card

I need a logo or design for 2 x 2 sq business cards and post cards for my Pediatric Occupational Therapy business. We work with children with special needs and help them learn skills for daily living (eating, writing, dressing, etc). We're looking for a colorful design (not loud) that looks professional and helps it stand out from other cards. I want to avoid many of the standard designs that you see on Nimbo press which are used my many other Pediatric OT's. The design will be intended for business cards, post cards and hopefully can also be used on company letterhead. I'll upload a current copy of the logo we currently use on company letter head so you get an idea of the design we've been using to date.

Font styles to use
Sans Serif

Requirements
Must have
• Area to include company name, address, phone, etc.
• Company name = Meadowlark Therapy Partners

```html
<!DOCTYPE html>
<html lang="en">
<head>
<meta charset="utf-8">
<title>Meadowlark Therapy Partners – Business Cards</title>
<link rel="stylesheet" href="https://fonts.googleapis.com/css2?family=Montserrat:wght@500;600;700&family=Amatic+SC:wght@700&display=swap">
<style>
  :root {
    --backdrop: #f1c40a;
    --card-white: #ffffff;
    --ink: #111111;
    --red: #e8415e;
    --orange: #f07f45;
    --yellow: #fcc72a;
    --teal: #5fbfa8;
    --sky: #55b3e4;
    --indigo: #6363a8;
    --violet: #9159a6;
  }
  * { box-sizing: border-box; margin: 0; padding: 0; }
  html, body { width: 1200px; height: 1200px; overflow: hidden; }
  body {
    background: var(--backdrop);
    position: relative;
    font-family: "Montserrat", sans-serif;
  }
  .card {
    position: absolute;
    top: 364px;
    width: 468px;
    height: 468px;
    overflow: hidden;
  }
  /* Contact side */
  .card-contact {
    left: 68px;
    background: var(--card-white);
    text-align: center;
  }
  .person-name {
    position: absolute;
    top: 62px;
    left: 0; right: 0;
    font-family: "Amatic SC", sans-serif;
    font-weight: 700;
    font-size: 54px;
    letter-spacing: 2px;
    color: var(--ink);
    line-height: 1;
  }
  .credentials {
    position: absolute;
    top: 112px;
    left: 0; right: 0;
    font-size: 18px;
    font-weight: 500;
    letter-spacing: 1px;
    color: var(--ink);
  }
  .name-rule {
    position: absolute;
    top: 142px;
    left: 148px;
    width: 172px;
    height: 5px;
    background: var(--ink);
  }
  .contact-list {
    position: absolute;
    top: 186px;
    left: 0; right: 0;
    list-style: none;
    font-size: 20px;
    font-weight: 500;
    letter-spacing: 1.5px;
    color: var(--ink);
    line-height: 24px;
  }
  .contact-list li {
    display: flex;
    align-items: center;
    justify-content: center;
    gap: 3px;
  }
  .contact-list svg { width: 17px; height: 17px; flex: none; }
  .hands-art {
    position: absolute;
    left: 16px;
    right: 6px;
    bottom: 0;
    height: 186px;
    background: linear-gradient(90deg, var(--red), var(--orange), var(--yellow), var(--teal), var(--sky), var(--indigo), var(--violet));
    opacity: 0.85;
  }
  /* Brand side */
  .card-brand {
    left: 640px;
    display: flex;
  }
  .stripe { flex: 1; height: 100%; }
  .stripe-red { background: var(--red); }
  .stripe-orange { background: var(--orange); }
  .stripe-yellow { background: var(--yellow); }
  .stripe-teal { background: var(--teal); }
  .stripe-sky { background: var(--sky); }
  .stripe-indigo { background: var(--indigo); }
  .stripe-violet { background: var(--violet); }
  .brand-name {
    position: absolute;
    top: 104px;
    left: 0; right: 0;
    text-align: center;
    font-weight: 700;
    font-size: 34px;
    line-height: 1.15;
    color: var(--card-white);
  }
  .brand-tagline {
    position: absolute;
    top: 378px;
    left: 0; right: 0;
    text-align: center;
    font-weight: 700;
    font-size: 17px;
    letter-spacing: -0.3px;
    color: var(--card-white);
  }
</style>
</head>
<body>
  <section class="card card-contact">
    <h1 class="person-name">Rosalind Ortega</h1>
    <p class="credentials">OTR/L</p>
    <div class="name-rule"></div>
    <ul class="contact-list">
      <li>
        <svg viewBox="0 0 20 20" aria-hidden="true"><circle cx="10" cy="10" r="10" fill="#e8415e"/><path d="M6.5 5.5l2 0 1 2.5-1.3 1a6 6 0 0 0 3 3l1-1.3 2.5 1v2c0 .6-.5 1-1 1A9 9 0 0 1 5.5 6.5c0-.6.4-1 1-1z" fill="#fff"/></svg>
        <span>305.555.0142</span>
      </li>
      <li>
        <svg viewBox="0 0 20 20" aria-hidden="true"><circle cx="10" cy="10" r="10" fill="#9159a6"/><rect x="5" y="6.5" width="10" height="7" fill="#fff"/><path d="M5 6.5l5 4 5-4" fill="none" stroke="#9159a6" stroke-width="1.2"/></svg>
        <span>rosieo14@mailbox.net</span>
      </li>
    </ul>
    <div class="hands-art" role="img" aria-label="Row of raised hands in rainbow colours"></div>
  </section>

  <section class="card card-brand">
    <div class="stripe stripe-red"></div>
    <div class="stripe stripe-orange"></div>
    <div class="stripe stripe-yellow"></div>
    <div class="stripe stripe-teal"></div>
    <div class="stripe stripe-sky"></div>
    <div class="stripe stripe-indigo"></div>
    <div class="stripe stripe-violet"></div>
    <h2 class="brand-name">Meadowlark Therapy<br>Partners</h2>
    <p class="brand-tagline">PEDIATRIC OCCUPATIONAL THERAPY</p>
  </section>
</body>
</html>
```